Dellavon Brokerage LLC product offerings and how to contact for quotes

A marketing email to new and current clients explaining the products the MGA offers and it's exclusive programs. Looking for a modern/sleek design that catches the eye and doesn't become the traditional spam email. Needs to have hyper links to website.
You can use the current website for details of product offerings for insurance: www.dellavon-example.com.
Target Market(s)
Long haul trucking
Industry/Entity Type
Trucking
Colors
0054AA
0677BA
7BADD7
CADEEF
E8F1F8
Requirements
Must have
- Color theme, informative, use of trucking art. Links to website.
Nice to have
- Catchy subject line; want to catch readers eye

```html
<!DOCTYPE html>
<html lang="en">
<head>
<meta charset="utf-8">
<title>Dellavon Brokerage LLC – Products</title>
<link href="https://fonts.googleapis.com/css2?family=Fira+Sans:wght@700;800&family=Inter:wght@400;500&display=swap" rel="stylesheet">
<style>
  :root {
    --sky: #1da8e6;
    --navy: #0a479b;
    --brand: #0054aa;
    --mid: #0677ba;
    --soft: #7badd7;
    --pale: #cadeef;
    --mist: #e8f1f8;
    --ink: #1d1d1f;
    --white: #ffffff;
  }
  * { margin: 0; padding: 0; box-sizing: border-box; }
  html, body { width: 1200px; height: 842px; overflow: hidden; }
  body { background: var(--sky); position: relative; font-family: "Inter", sans-serif; color: var(--ink); }
  a { color: inherit; text-decoration: none; }

  .page { position: absolute; top: 50px; width: 521px; height: 737px; background: var(--white); overflow: hidden; }
  .page--about { left: 48px; }
  .page--products { left: 624px; }

  .brand { position: absolute; top: 0; left: 0; width: 100%; height: 101px; display: flex; align-items: center; justify-content: center; gap: 9px; }
  .brand__dot { width: 14px; height: 14px; background: var(--brand); }
  .brand__name { font-family: "Fira Sans", sans-serif; font-weight: 800; font-size: 30px; color: var(--brand); letter-spacing: 0.5px; }

  .hero { position: absolute; top: 101px; left: 0; width: 521px; height: 340px; }
  .hero__title { position: absolute; top: 163px; left: 26px; font-family: "Fira Sans", sans-serif; font-weight: 800; font-size: 26px; line-height: 30px; color: var(--white); text-shadow: 0 1px 3px rgba(0,0,0,0.35); text-transform: uppercase; }

  .section-title { font-family: "Fira Sans", sans-serif; font-weight: 800; color: var(--brand); text-align: center; text-transform: uppercase; }
  .divider { display: flex; align-items: center; justify-content: center; gap: 4px; }
  .divider__line { width: 42px; height: 1px; background: var(--brand); }
  .divider__mark { width: 7px; height: 7px; border-radius: 50%; background: var(--mid); }

  .about__title { position: absolute; top: 428px; left: 0; width: 100%; font-size: 21px; }
  .about__divider { position: absolute; top: 466px; left: 0; width: 100%; }
  .about__body { position: absolute; top: 488px; left: 26px; width: 470px; font-size: 10.4px; line-height: 14.4px; text-align: justify; }
  .about__body p + p { margin-top: 14px; }

  .contact-bar { position: absolute; bottom: 0; left: 0; width: 100%; height: 69px; background: var(--navy); display: flex; align-items: center; justify-content: space-around; padding: 0 14px; color: var(--white); font-size: 10.6px; }
  .contact-bar__item { display: flex; align-items: center; gap: 6px; }
  .contact-bar__icon { width: 13px; height: 13px; }

  .products__title { position: absolute; top: 24px; left: 0; width: 100%; font-size: 27px; letter-spacing: 0.3px; }
  .products__divider { position: absolute; top: 68px; left: 0; width: 100%; }
  .products__divider .divider__line { width: 44px; }

  .product { position: absolute; left: 22px; width: 470px; height: 103px; }
  .product__frame { position: absolute; left: 48px; top: 0; right: 0; bottom: 0; border: 1px solid #2d63b4; border-radius: 16px; }
  .product__photo { position: absolute; left: 0; top: 0; width: 103px; height: 103px; border-radius: 50%; }
  .product__body { position: absolute; left: 119px; top: 12px; right: 14px; }
  .product__name { font-family: "Inter", sans-serif; font-weight: 600; font-size: 11.5px; color: var(--brand); margin-bottom: 8px; font-weight: 700; }
  .product__text { font-size: 10.2px; line-height: 14.4px; }
</style>
</head>
<body>

<section class="page page--about">
  <header class="brand">
    <span class="brand__dot"></span>
    <span class="brand__name">DELLAVON</span>
  </header>

  <svg class="hero" viewBox="0 0 521 340" aria-hidden="false">
    <defs>
      <linearGradient id="sunset" x1="0" y1="0" x2="0" y2="1">
        <stop offset="0" stop-color="#b7bfcc"/>
        <stop offset="0.3" stop-color="#d9c7b0"/>
        <stop offset="0.5" stop-color="#e7a865"/>
        <stop offset="0.62" stop-color="#6d6359"/>
        <stop offset="0.8" stop-color="#6e6f73"/>
        <stop offset="1" stop-color="#4a4a4d"/>
      </linearGradient>
    </defs>
    <polygon role="img" aria-label="Photo of a semi truck driving along a mountain highway at sunset" fill="url(#sunset)" points="0,0 521,0 521,262 470,327 0,226"/>
    <polygon fill="#1f77c9" points="0,226 470,327 450,336 0,243"/>
    <polygon fill="#1da8e6" points="521,262 521,282 485,330 450,336 470,327"/>
    <polygon fill="#1a5fae" points="450,336 470,327 485,330 478,334"/>
  </svg>
  <h1 class="hero__title">Your partner for<br>complex risks,<br>backed by<br>superior service</h1>

  <h2 class="section-title about__title">Who we are</h2>
  <div class="divider about__divider"><span class="divider__line"></span><span class="divider__mark"></span><span class="divider__line"></span></div>
  <div class="about__body">
    <p>At Dellavon Brokerage, LLC, we are a boutique Managing General Agent (MGA) specializing in commercial insurance tailored for the trucking industry. Our company was established with a clear mission: to support small, independent trucking retailers facing challenging risks, while delivering an exceptional customer service experience.</p>
    <p>With deep knowledge and expertise in every facet of trucking operations, we are the preferred choice for our clients. We believe in maintaining close communication; you can always count on a prompt response to your emails or phone calls. Our straightforward philosophy involves partnering with a select group of quality retail agencies strategically located across the United States. This allows us to provide focused, high-quality service to our clients.</p>
  </div>

  <footer class="contact-bar">
    <span class="contact-bar__item"><svg class="contact-bar__icon" viewBox="0 0 14 14"><circle cx="7" cy="7" r="7" fill="#fff"/><rect x="4.6" y="3" width="4.8" height="8" rx="1" fill="none" stroke="#0a479b" stroke-width="1.2"/></svg>(555)014-2286</span>
    <span class="contact-bar__item"><svg class="contact-bar__icon" viewBox="0 0 14 14"><circle cx="7" cy="7" r="7" fill="#fff"/><rect x="3.5" y="4.5" width="7" height="5" fill="none" stroke="#0a479b" stroke-width="1.1"/><path d="M3.5 4.5 7 7.5 10.5 4.5" fill="none" stroke="#0a479b" stroke-width="1.1"/></svg>hello@dellavon-example.com</span>
    <a class="contact-bar__item" href="https://www.dellavon-example.com"><svg class="contact-bar__icon" viewBox="0 0 14 14"><circle cx="7" cy="7" r="7" fill="#fff"/><circle cx="7" cy="7" r="4" fill="none" stroke="#0a479b" stroke-width="1"/><ellipse cx="7" cy="7" rx="1.8" ry="4" fill="none" stroke="#0a479b" stroke-width="0.9"/><path d="M3 7h8" stroke="#0a479b" stroke-width="0.9"/></svg>www.dellavon-example.com</a>
  </footer>
</section>

<section class="page page--products">
  <h2 class="section-title products__title">Our products</h2>
  <div class="divider products__divider"><span class="divider__line"></span><span class="divider__mark"></span><span class="divider__line"></span></div>

  <article class="product" style="top:96px">
    <div class="product__frame"></div>
    <div class="product__photo" role="img" aria-label="Photo of white semi trucks parked at a loading dock" style="background:linear-gradient(160deg,#9aa7b6,#e4e7ea 45%,#6d747c)"></div>
    <div class="product__body">
      <h3 class="product__name">Auto Liability</h3>
      <p class="product__text">Liability insurance is a part of the general insurance system of risk financing to protect the purchaser (the "insured") from the risks of liabilities imposed by lawsuits and similar claims.</p>
    </div>
  </article>

  <article class="product" style="top:224px">
    <div class="product__frame"></div>
    <div class="product__photo" role="img" aria-label="Photo of two drivers reviewing paperwork beside a truck" style="background:linear-gradient(120deg,#c9c4bd,#8c7a66 45%,#7aa36a 70%,#3d4750)"></div>
    <div class="product__body">
      <h3 class="product__name">Non-Trucking Liability</h3>
      <p class="product__text">Non-Trucking Liability (NTL) provides coverage in case you cause an accident while you are using your vehicle for non-business or personal use other than transporting goods or merchandise.</p>
    </div>
  </article>

  <article class="product" style="top:351px">
    <div class="product__frame"></div>
    <div class="product__photo" role="img" aria-label="Photo of a tanker truck on a highway" style="background:linear-gradient(135deg,#5c5f66,#9aa3ad 45%,#c9b08a 65%,#5a5a5d)"></div>
    <div class="product__body">
      <h3 class="product__name">Auto Physical Damage</h3>
      <p class="product__text">Physical Damage insurance is a type of insurance that covers damages to your truck and trailer. This type of coverage is typically offered as part of an auto insurance policy.</p>
    </div>
  </article>

  <article class="product" style="top:478px">
    <div class="product__frame"></div>
    <div class="product__photo" role="img" aria-label="Photo of a trailer backed into a warehouse loading bay" style="background:linear-gradient(135deg,#6b5a4a,#c9a982 40%,#d9d9dc 60%,#4a4644)"></div>
    <div class="product__body">
      <h3 class="product__name">Motor Truck Cargo</h3>
      <p class="product__text">Provides liability insurance for truckers who carry the cargo of others and is used in the event that the cargo is destroyed, damaged, stolen, or otherwise declared a loss while in the process</p>
    </div>
  </article>

  <footer class="contact-bar">
    <span class="contact-bar__item"><svg class="contact-bar__icon" viewBox="0 0 14 14"><circle cx="7" cy="7" r="7" fill="#fff"/><rect x="4.6" y="3" width="4.8" height="8" rx="1" fill="none" stroke="#0a479b" stroke-width="1.2"/></svg>(555)014-2286</span>
    <span class="contact-bar__item"><svg class="contact-bar__icon" viewBox="0 0 14 14"><circle cx="7" cy="7" r="7" fill="#fff"/><rect x="3.5" y="4.5" width="7" height="5" fill="none" stroke="#0a479b" stroke-width="1.1"/><path d="M3.5 4.5 7 7.5 10.5 4.5" fill="none" stroke="#0a479b" stroke-width="1.1"/></svg>hello@dellavon-example.com</span>
    <a class="contact-bar__item" href="https://www.dellavon-example.com"><svg class="contact-bar__icon" viewBox="0 0 14 14"><circle cx="7" cy="7" r="7" fill="#fff"/><circle cx="7" cy="7" r="4" fill="none" stroke="#0a479b" stroke-width="1"/><ellipse cx="7" cy="7" rx="1.8" ry="4" fill="none" stroke="#0a479b" stroke-width="0.9"/><path d="M3 7h8" stroke="#0a479b" stroke-width="0.9"/></svg>www.dellavon-example.com</a>
  </footer>
</section>

</body>
</html>
```